Design for sports training app

We need the design for 9 screens of an app that supports trainers of sport teams in preparing their training sessions. Regarding colors, fonts etc. there is absolute freedom for the designer to choose what he thinks is best.
The app will be called "Plomix", our idea for the logo is something like a stopwatch.
Wireframes are attached for every screen. You don't have to stick to those - if you have better ideas, we are happy to see them.
Our strategy is "mobile first". Based on the app design we will create a homepage later - I guess it makes sense to give this to the same person, let's see.
The deliverables are attached.
All in all the main target is to present a very simple, intuitive and nice UI that the user can work with without much learning.
Updates
Target Market(s)
Soccer trainers
Industry/Entity Type
Training
Look and feel

```html
<!DOCTYPE html>
<html lang="en">
<head>
<meta charset="utf-8">
<title>Plomix – App Screens</title>
<link href="https://fonts.googleapis.com/css2?family=Roboto+Condensed:wght@300;400&family=Roboto:wght@500&display=swap" rel="stylesheet">
<style>
  :root {
    --page-bg: #f1f1f1;
    --bar-bg: #f7f7f7;
    --ink: #111111;
    --accent: #1f5fa6;
    --grad-top: #2063a7;
    --grad-bottom: #001a5e;
    --track-fill: #63a6df;
    --thumb: #6aaee4;
    --white: #ffffff;
    --row-text: #3b77b8;
    --footer-bg: #e6e6ea;
    --battery: #2bd84a;
  }
  * { box-sizing: border-box; margin: 0; padding: 0; }
  html, body { width: 1200px; height: 800px; overflow: hidden; }
  body {
    background: var(--page-bg);
    font-family: "Roboto Condensed", "Arial Narrow", sans-serif;
    display: flex;
    justify-content: center;
    align-items: center;
    gap: 50px;
  }
  .screen {
    position: relative;
    width: 350px;
    height: 620px;
    background: linear-gradient(180deg, var(--grad-top) 0%, var(--grad-bottom) 100%);
    overflow: hidden;
    box-shadow: 0 8px 30px rgba(0,0,0,0.12);
  }
  .status-bar {
    position: absolute; left: 0; top: 0; width: 100%; height: 20px;
    background: var(--bar-bg);
    font-family: "Roboto", sans-serif; font-weight: 500; font-size: 12px;
    color: var(--ink);
    display: flex; align-items: center; justify-content: space-between;
    padding: 0 6px;
  }
  .status-bar .signal { letter-spacing: -1px; }
  .status-bar .signal span { letter-spacing: 0; margin-left: 3px; }
  .status-bar .time { position: absolute; left: 50%; transform: translateX(-50%); }
  .status-bar .battery { display: flex; align-items: center; gap: 3px; }
  .nav-bar {
    position: absolute; left: 0; top: 20px; width: 100%; height: 51px;
    background: var(--bar-bg);
    display: flex; align-items: center; justify-content: center;
  }
  .nav-bar .back { position: absolute; left: 16px; top: 17px; }
  .nav-bar h1 { font-weight: 400; font-size: 14px; color: var(--accent); }

  .skills { position: absolute; left: 0; top: 71px; width: 100%; }
  .skill { position: relative; height: 53px; }
  .skill-label {
    position: absolute; top: 12px; width: 100%; text-align: center;
    font-size: 11px; color: var(--white); font-weight: 300; padding-right: 14px;
  }
  .track {
    position: absolute; left: 42px; top: 38px; width: 267px; height: 2px;
    background: linear-gradient(90deg, var(--track-fill) 0 49%, var(--white) 49% 100%);
  }
  .thumb {
    position: absolute; left: 121px; top: -10px; width: 22px; height: 22px;
    border-radius: 50%; background: var(--thumb);
  }

  .rows { position: absolute; left: 38px; top: 113px; width: 270px; display: flex; flex-direction: column; gap: 6px; }
  .row {
    height: 31px; border-radius: 16px; background: var(--white);
    display: flex; align-items: center; justify-content: space-between;
    padding: 0 16px 0 19px; font-size: 12px; color: var(--row-text); font-weight: 300;
  }
  .row .stepper { display: flex; gap: 4px; }
  .row.outline { background: transparent; border: 1px solid rgba(255,255,255,0.7); color: var(--white); }
  .settings-rows { top: 102px; gap: 6px; }

  .log-out {
    position: absolute; left: 0; bottom: 0; width: 100%; height: 53px;
    background: var(--footer-bg);
    display: flex; align-items: center; justify-content: center;
    font-size: 12px; color: var(--accent); font-weight: 300;
  }
</style>
</head>
<body>

<section class="screen skills-screen">
  <div class="status-bar">
    <div class="signal">●●●●●<span>3G</span></div>
    <div class="time">1:52</div>
    <div class="battery">100 %
      <svg width="30" height="10" viewBox="0 0 30 10"><rect x="0.5" y="0.5" width="25" height="9" rx="1.5" fill="var(--battery)" stroke="#333"/><rect x="26" y="3" width="2" height="4" fill="#333"/></svg>
    </div>
  </div>
  <header class="nav-bar">
    <svg class="back" width="10" height="17" viewBox="0 0 10 17"><path d="M8.5 1 1.5 8.5 8.5 16" fill="none" stroke="var(--accent)" stroke-width="1.5"/></svg>
    <h1>Plomix skills</h1>
  </header>
  <div class="skills">
    <div class="skill"><p class="skill-label">Coordination</p><div class="track"><span class="thumb"></span></div></div>
    <div class="skill"><p class="skill-label">Finishing</p><div class="track"><span class="thumb"></span></div></div>
    <div class="skill"><p class="skill-label">Stamina</p><div class="track"><span class="thumb"></span></div></div>
    <div class="skill"><p class="skill-label">Speed</p><div class="track"><span class="thumb"></span></div></div>
    <div class="skill"><p class="skill-label">Understanding of the game</p><div class="track"><span class="thumb"></span></div></div>
    <div class="skill"><p class="skill-label">Defensing Behavior</p><div class="track"><span class="thumb"></span></div></div>
  </div>
</section>

<section class="screen conditions-screen">
  <div class="status-bar">
    <div class="signal">●●●●●<span>3G</span></div>
    <div class="time">1:52</div>
    <div class="battery">100 %
      <svg width="30" height="10" viewBox="0 0 30 10"><rect x="0.5" y="0.5" width="25" height="9" rx="1.5" fill="var(--battery)" stroke="#333"/><rect x="26" y="3" width="2" height="4" fill="#333"/></svg>
    </div>
  </div>
  <header class="nav-bar">
    <svg class="back" width="10" height="17" viewBox="0 0 10 17"><path d="M8.5 1 1.5 8.5 8.5 16" fill="none" stroke="var(--accent)" stroke-width="1.5"/></svg>
    <h1>Conditions</h1>
  </header>
  <div class="rows">
    <div class="row"><span>Cones</span><span class="stepper"><span>+</span><span>20</span><span>–</span></span></div>
    <div class="row"><span>Goals</span><span class="stepper"><span>+</span><span>&nbsp;5</span><span>–</span></span></div>
    <div class="row"><span>Players</span><span class="stepper"><span>+</span><span>10</span><span>–</span></span></div>
    <div class="row"><span>Goalies</span><span class="stepper"><span>+</span><span>&nbsp;2</span><span>–</span></span></div>
  </div>
</section>

<section class="screen settings-screen">
  <div class="status-bar">
    <div class="signal">●●●●●<span>3G</span></div>
    <div class="time">1:52</div>
    <div class="battery">100 %
      <svg width="30" height="10" viewBox="0 0 30 10"><rect x="0.5" y="0.5" width="25" height="9" rx="1.5" fill="var(--battery)" stroke="#333"/><rect x="26" y="3" width="2" height="4" fill="#333"/></svg>
    </div>
  </div>
  <header class="nav-bar">
    <svg class="back" width="10" height="17" viewBox="0 0 10 17"><path d="M8.5 1 1.5 8.5 8.5 16" fill="none" stroke="var(--accent)" stroke-width="1.5"/></svg>
    <h1>Settings</h1>
  </header>
  <div class="rows settings-rows">
    <div class="row outline"><span>Velmora United - Juniors - Logged</span></div>
    <div class="row"><span>Legal</span><svg width="7" height="12" viewBox="0 0 7 12"><path d="M1 1l5 5-5 5" fill="none" stroke="var(--row-text)" stroke-width="1.2"/></svg></div>
    <div class="row"><span>Share</span><svg width="7" height="12" viewBox="0 0 7 12"><path d="M1 1l5 5-5 5" fill="none" stroke="var(--row-text)" stroke-width="1.2"/></svg></div>
  </div>
  <footer class="log-out">LOG OUT</footer>
</section>

</body>
</html>
```